Software engineering company needs business card

I need a cool business card. Company: Byte Merano Larchwood Ave 41 58213 Dunmere Name: Gerald Hofmann CEO / Managing Director & Owner

Industry/Entity Type

Business

```html
<!DOCTYPE html>
<html lang="de">
<head>
<meta charset="utf-8">
<title>Byte Merano – Visitenkarte</title>
<link href="https://fonts.googleapis.com/css2?family=Open+Sans:wght@400;600&display=swap" rel="stylesheet">
<style>
  :root {
    --backdrop: #2b1c16;
    --card: #0b0c0c;
    --green: #8cc63f;
    --grey: #a7a9ab;
    --grey-light: #c4c6c8;
    --grey-dark: #3a3b3c;
    --divider: #5a5b5d;
  }
  * { margin: 0; padding: 0; box-sizing: border-box; }
  html, body {
    width: 1200px; height: 1000px; overflow: hidden;
    background: var(--backdrop);
    font-family: "Open Sans", Arial, sans-serif;
  }
  .card {
    position: absolute;
    width: 500px; height: 286px;
    background: var(--card);
    border-radius: 22px;
    overflow: hidden;
  }
  .card--front { left: 80px; top: 357px; }
  .card--back { left: 620px; top: 357px; }

  .brand {
    position: absolute; left: 0; top: 0; width: 230px; height: 100%;
    display: flex; align-items: center; justify-content: center; gap: 10px;
  }
  .brand__dot { width: 14px; height: 14px; background: var(--green); }
  .brand__name { color: var(--green); font-size: 21px; font-weight: 400; letter-spacing: 1px; }

  .divider {
    position: absolute; left: 238px; top: 58px; width: 1px; height: 170px;
    background: var(--divider);
  }
  .details { position: absolute; left: 262px; top: 62px; color: var(--grey); }
  .details__name { font-size: 23px; font-weight: 600; line-height: 1.1; color: var(--grey-light); }
  .details__name .surname { color: var(--green); }
  .details__role { font-size: 12px; margin-top: 3px; }
  .details__contact { font-size: 12px; line-height: 1.45; margin-top: 20px; }
  .details__address { font-size: 12px; line-height: 1.45; margin-top: 14px; color: var(--green); }

  .back-pattern {
    position: absolute; inset: 0;
    background: radial-gradient(circle at 50% 50%, var(--card) 0, var(--card) 56%, var(--grey-dark) 100%);
  }
  .back-brand {
    position: absolute; inset: 0;
    display: flex; align-items: center; justify-content: center;
    color: var(--green); font-size: 34px; font-weight: 600; letter-spacing: 1px;
  }
</style>
</head>
<body>
  <section class="card card--front">
    <div class="brand">
      <span class="brand__dot"></span>
      <span class="brand__name">Byte Merano</span>
    </div>
    <div class="divider"></div>
    <div class="details">
      <p class="details__name">Gerald <span class="surname">Hofmann</span></p>
      <p class="details__role">CEO / Geschäftsführer &amp; Inhaber</p>
      <p class="details__contact">+12 480 552 9031<br>hello@bytemerano.com<br>www.bytemerano.com</p>
      <p class="details__address">Byte Merano, Larchwood Ave 41<br>58213 Dunmere</p>
    </div>
  </section>

  <section class="card card--back">
    <div class="back-pattern" role="img" aria-label="Decorative grey pattern framing the card centre"></div>
    <div class="back-brand">Byte Merano</div>
  </section>
</body>
</html>
```